Ridgeline Outfitters Business Cards

Recently had a logo done with Artfolio and now looking for a business card to go along with it.

Target Market(s)

Ridgeline Outfitters is a weapons dealer. My market will be primarily men, hunting, shooting type.

Industry/Entity Type

Business

Contact Information for Business Card

I selected double sided, but this is not required, single or double is going to be fine. I picture the logo on one side, or perhaps just the circle which contains "RO" with the remaining info on the other side.

Font styles to use
Sans Serif

Requirements
Must have
• My name: Milo Brandt
• Title: Owner
• tel: 612-555-0187
• web: www.ridgelineoutfittersmn.example
Nice to have
• I like the concept of a black business card. I would like to keep the colors monotone, black, grey, white or red. Red is acceptable because it is in the logo. I have also seen cards that are matte black with shiny black as well, perhaps for the logo (or circle RO) part of the logo.
• I will upload a couple of the logos for use, and also an example I just found of the black on black. and some others that have a nice contrast.
Should not have
• lots of colors are not wanted.

```html
<!DOCTYPE html>
<html lang="en">
<head>
<meta charset="utf-8">
<title>Ridgeline Outfitters Business Card</title>
<link rel="stylesheet" href="https://fonts.googleapis.com/css2?family=Open+Sans:wght@400;600&display=swap">
<style>
  :root {
    --backdrop: #5a5a5a;
    --card: #03040a;
    --red: #e3101e;
    --grey: #8c8c8c;
    --silver: #b9b9bd;
    --divider: #3a3a3e;
  }
  * { margin: 0; padding: 0; box-sizing: border-box; }
  html, body { width: 1200px; height: 1200px; overflow: hidden; }
  body {
    background: var(--backdrop);
    font-family: "Open Sans", sans-serif;
    position: relative;
  }
  .card {
    position: absolute;
    left: 260px;
    width: 680px;
    height: 386px;
    background: var(--card);
  }
  .card--front { top: 190px; }
  .card--back { top: 624px; }

  .front-mark {
    position: absolute;
    inset: 0;
    display: flex;
    align-items: center;
    justify-content: center;
    gap: 22px;
  }
  .front-mark__ring { width: 120px; height: 120px; }
  .front-mark__name {
    color: var(--silver);
    font-weight: 600;
    font-size: 28px;
  }

  .brand {
    position: absolute;
    left: 32px;
    top: 150px;
    display: flex;
    align-items: center;
    gap: 12px;
  }
  .brand__ring { width: 84px; height: 84px; }
  .brand__name {
    color: var(--red);
    font-weight: 600;
    font-size: 21px;
    white-space: nowrap;
  }

  .divider {
    position: absolute;
    left: 380px;
    top: 124px;
    width: 1px;
    height: 138px;
    background: var(--divider);
  }
  .contact {
    position: absolute;
    left: 398px;
    top: 136px;
  }
  .contact__name {
    color: var(--red);
    font-size: 24px;
    font-weight: 400;
    line-height: 1.2;
  }
  .contact__title {
    color: var(--grey);
    font-size: 16px;
    line-height: 1.3;
    margin-bottom: 12px;
  }
  .contact__line {
    display: flex;
    align-items: center;
    gap: 9px;
    color: var(--grey);
    font-size: 14.5px;
    line-height: 23px;
    white-space: nowrap;
  }
  .contact__icon { width: 14px; height: 14px; flex: none; }
</style>
</head>
<body>
  <section class="card card--front">
    <div class="front-mark">
      <svg class="front-mark__ring" viewBox="0 0 120 120" aria-hidden="true">
        <circle cx="60" cy="60" r="55" fill="none" stroke="var(--silver)" stroke-width="6"/>
      </svg>
      <span class="front-mark__name">Ridgeline Outfitters</span>
    </div>
  </section>

  <section class="card card--back">
    <div class="brand">
      <svg class="brand__ring" viewBox="0 0 84 84" aria-hidden="true">
        <circle cx="42" cy="42" r="38" fill="none" stroke="var(--grey)" stroke-width="5"/>
      </svg>
      <span class="brand__name">Ridgeline Outfitters</span>
    </div>

    <div class="divider"></div>

    <div class="contact">
      <p class="contact__name">Milo Brandt</p>
      <p class="contact__title">Owner</p>
      <p class="contact__line">
        <svg class="contact__icon" viewBox="0 0 16 16" aria-hidden="true">
          <path d="M1 6 C1 2 15 2 15 6 L12 7 L11 5 H5 L4 7 Z" fill="var(--red)"/>
          <path d="M4 8 H12 L14 14 H2 Z" fill="var(--red)"/>
          <circle cx="8" cy="11" r="1.6" fill="var(--card)"/>
        </svg>
        612-555-0187
      </p>
      <p class="contact__line">
        <svg class="contact__icon" viewBox="0 0 16 16" aria-hidden="true">
          <g fill="none" stroke="var(--red)" stroke-width="1.3">
            <circle cx="8" cy="8" r="6.8"/>
            <ellipse cx="8" cy="8" rx="3" ry="6.8"/>
            <line x1="1.2" y1="8" x2="14.8" y2="8"/>
            <line x1="2.5" y1="4.5" x2="13.5" y2="4.5"/>
            <line x1="2.5" y1="11.5" x2="13.5" y2="11.5"/>
          </g>
        </svg>
        www.ridgelineoutfittersmn.example
      </p>
    </div>
  </section>
</body>
</html>
```